Stationery Design Project

see attached logo and business card layout, envelopes, letterhead, proposal, and invoice stationery needs to all flow.

Industry/Entity Type

Business

```html
<!DOCTYPE html>
<html lang="en">
<head>
<meta charset="utf-8">
<title>Business Card – Account Manager</title>
<link rel="stylesheet" href="https://fonts.googleapis.com/css2?family=Arimo:wght@400&display=swap">
<style>
  :root {
    --card-black: #080909;
    --band-yellow: #f9e259;
    --address-white: #ffffff;
    --contact-ink: #242424;
  }
  html, body {
    margin: 0;
    padding: 0;
    width: 1200px;
    height: 684px;
    overflow: hidden;
    background: var(--card-black);
  }
  .business-card {
    display: block;
    width: 1200px;
    height: 684px;
    font-family: "Arimo", Arial, sans-serif;
  }
  .card-background { fill: var(--card-black); }
  .contact-band { fill: var(--band-yellow); }
  .street-address {
    fill: var(--address-white);
    font-size: 39px;
    letter-spacing: -0.3px;
  }
  .contact-line {
    fill: var(--contact-ink);
    font-size: 34px;
  }
  .holder-title {
    fill: var(--contact-ink);
    font-size: 36px;
  }
</style>
</head>
<body>
<svg class="business-card" viewBox="0 0 1200 684" xmlns="http://www.w3.org/2000/svg">
  <rect class="card-background" x="0" y="0" width="1200" height="684"/>
  <text class="street-address" x="206" y="320" textLength="953">18400 MERIDIAN RD SUITE 200 ALDEN, CA 92071</text>
  <rect class="contact-band" x="163" y="322" width="1037" height="260"/>
  <g class="contact-details">
    <text class="contact-line phone" x="289" y="411">Tel : 555,214,6400</text>
    <text class="contact-line fax" x="748" y="411">Fax : 555,214,6402</text>
    <text class="contact-line cell" x="225" y="459">Cell : 555,730,9145</text>
    <text class="contact-line email" x="714" y="459">Email :Cell:555,730,9145</text>
  </g>
  <text class="holder-title" x="400" y="538">Marco Velasquez : Account Manager</text>
</svg>
</body>
</html>
```